Double Sided Business Card Design for Pet Services

My mom and I want to start a business for pets. We want to offer dog walking, pet sitting as well as boarding and grooming at our home. For the front of the business card, we want a logo that will capture all of our services. We want the name to be Bigotes, Inc., which means little paws in Spanish. Perhaps, there could be little paws or just a little paw implemented within the word Bigotes. Or we would want a cat and a dog by the word Bigotes. We have a cat and a dog at home, and we would be really happy if they could be a part of the business card. It does not have to be anything crazy. Just an outline of a cat or a dog would be awesome. Please see uploaded file.
As for the back of the card, we would want little paws all over the card or we would want a collar, leash, grooming scissor, dog/cat bowl, bone, fish, or toy to show all of the services that we provide. Along with either the many paws or many pet objects, we would want to add our information, such as name (Lorenza Mireles), telephone numbers (555) 812-3762, e-mail addresses bigotesinc@correomail.net, etc.
We would also want a catch phrase to go on the back of the card, such as "Where all paws matter!" Or "We strive for happy tails." or "A paw-bulous service is guaranteed!"
As for colors, we would not want that many. We would want perhaps white and blue. We would want soft colors that will stand out and make an impression. The same goes with the text. An elegant text would be nice. Or perhaps a text with bold letters. We are excited to see the results, but we are also excited to see your creative ideas and what you will bring to the table.

Target Market(s)

Pet Owners

Contact Information for Business Card

For the front of the business card, we want a logo that will capture all of our services. We want the name to be Bigotes, Inc., which means little paws in Spanish. Perhaps, there could be little paws or just a little paw implemented within the word Bigotes. Or we would want a cat and a dog by the word Bigotes. We have a cat and a dog at home, and we would be really happy if they could be a part of the business card. It does not have to be anything crazy. Just an outline of a cat or a dog would be awesome. Please see uploaded file.
As for the back of the card, we would want little paws all over the card or we would want a collar, leash, grooming scissor, dog/cat bowl, bone, fish, or toy to show all of the services that we provide. Along with either the many paws or many pet objects, we would want to add our information, such as name, telephone numbers, e-mail addresses, etc. We would also want a catch phrase to go on the back of the card, such as "Where all paws matter!" Or "We strive happy tails." or "A paw-bulous service is guaranteed!" Or if there is a way to put the catch phrase in the front of the card. We are open to seeing variety.

Logo Text

Bigotes, Inc

Font styles to use
Serif
Script

Colors
ffffff
33a6d7
145ea8

Requirements
Must have
• My project must be a double sided business card.

```html
<!DOCTYPE html>
<html lang="en">
<head>
<meta charset="utf-8">
<title>Bigotes, Inc – Business Card</title>
<link rel="stylesheet" href="https://fonts.googleapis.com/css2?family=Cormorant+Garamond:ital,wght@0,600;1,500&family=Gudea&display=swap">
<style>
  :root {
    --page-bg: #ecebe8;
    --card-white: #ffffff;
    --paw-pattern-light: #fbeaea;
    --card-blue: #7fa3d9;
    --paw-pattern-blue: #7598cf;
    --accent-orange: #f0901e;
    --ink: #1c1c1c;
    --subtitle-ink: #4a5a72;
    --cat-grey: #8a8d92;
    --dog-orange: #f08a1e;
  }
  * { box-sizing: border-box; margin: 0; padding: 0; }
  html, body { width: 1200px; height: 800px; overflow: hidden; }
  body {
    background: var(--page-bg);
    display: flex;
    align-items: center;
    justify-content: center;
    gap: 60px;
  }
  .card {
    position: relative;
    width: 520px;
    height: 297px;
    border-radius: 4px;
    overflow: hidden;
    box-shadow: 0 6px 18px rgba(0,0,0,0.15);
  }

  /* Back side */
  .card-back { background: var(--card-white); }
  .card-back .paw-pattern {
    position: absolute; inset: 0;
    background: var(--paw-pattern-light);
  }
  .contact {
    position: absolute;
    left: 190px;
    top: 78px;
  }
  .contact-name {
    font-family: "Cormorant Garamond", serif;
    font-weight: 600;
    font-size: 26px;
    color: var(--accent-orange);
    letter-spacing: 0.5px;
  }
  .contact-phone {
    font-family: "Gudea", sans-serif;
    font-size: 25px;
    color: var(--ink);
    margin-top: 6px;
  }
  .contact-email {
    font-family: "Gudea", sans-serif;
    font-size: 15px;
    color: var(--ink);
    margin-top: 2px;
  }
  .tagline {
    position: absolute;
    left: 150px;
    bottom: 44px;
    font-family: "Cormorant Garamond", serif;
    font-style: italic;
    font-weight: 500;
    font-size: 23px;
    color: var(--accent-orange);
  }

  /* Front side */
  .card-front { background: var(--card-blue); }
  .card-front .paw-pattern {
    position: absolute; inset: 0;
    background: var(--paw-pattern-blue);
  }
  .pet-illustration {
    position: absolute;
    border-radius: 40%;
  }
  .pet-cat {
    left: 40px; top: 66px;
    width: 96px; height: 120px;
    background: var(--cat-grey);
  }
  .pet-dog {
    right: 36px; top: 128px;
    width: 100px; height: 104px;
    background: var(--dog-orange);
  }
  .brand {
    position: absolute;
    left: 146px;
    top: 112px;
    width: 232px;
    text-align: center;
  }
  .brand-name {
    font-family: "Cormorant Garamond", serif;
    font-weight: 600;
    font-size: 42px;
    line-height: 1;
    color: var(--ink);
    white-space: nowrap;
  }
  .brand-subtitle {
    font-family: "Cormorant Garamond", serif;
    font-weight: 600;
    font-size: 18px;
    letter-spacing: 5px;
    color: var(--subtitle-ink);
    margin-top: 8px;
    white-space: nowrap;
  }
</style>
</head>
<body>
  <section class="card card-back">
    <div class="paw-pattern" role="img" aria-label="Repeating pattern of soft pink paw prints on white"></div>
    <div class="contact">
      <p class="contact-name">Lorenza Mireles</p>
      <p class="contact-phone">(555) 812-3762</p>
      <p class="contact-email">bigotesinc@correomail.net</p>
    </div>
    <p class="tagline">A paw-bulous service is guaranteed!</p>
  </section>

  <section class="card card-front">
    <div class="paw-pattern" role="img" aria-label="Repeating pattern of darker blue paw prints on blue"></div>
    <div class="pet-illustration pet-cat" role="img" aria-label="Cartoon grey tabby kitten sitting"></div>
    <div class="brand">
      <p class="brand-name">Bigotes, Inc</p>
      <p class="brand-subtitle">Pet Services</p>
    </div>
    <div class="pet-illustration pet-dog" role="img" aria-label="Cartoon orange puppy sitting"></div>
  </section>
</body>
</html>
```